WordPress Website Design & Theme - The Meridale Bidding House

Need a WordPress design for an auction company wanting a responsive, simple and easy to use site.

Please keep in mind that the design will be built on a responsive WP theme.

Colors will be light or white and complimentary/highlight colors from the logo.

Industry/Entity Type

It Company

Number of Pages Required

1 page

Font styles to use
Serif
Sans Serif

Requirements
Must have
• Navigation - 1) Home 2) Auction Calendar 3) Auction Results 4) For Sale 5) Services 6)About Us 7) Contact Us
• A site they mention liking is http://www.quenbrookbids.example/
• Site will have full width slideshow 960px. Use stock real estate photo. Header will have logo (attached) and contact info:
• THE MERIDALE BIDDING HOUSE
• P.O. Box 582
• Brinmoor, OK 35817
• PHONE: (800)615-3087 or (256)382-9061
• FAX: (256)382-5148
• EMAIL: info@meridale-bidding.example
• There will be no sidebar on the homepage. There can be 3 horizontal widgets for "featured Listings", Join Our Newsletter, and maybe a form like http://www.meridale-bidding.example/request_proposal.php. The "Upcoming Auctions" feature as is seen on http://www.quenbrookbids.example/ will be used (attached image).
• In the footer: contact info, social media (FB, twitter, RSS), affiliation logos (attached), perhaps smaller company logo, News & Events blog, and if room "Featured Auctions".
Nice to have
• Use of drop-down menus styling- 1) Live Auctions 2) Online Auctions - under the Auction Calendar tab

```html
<!DOCTYPE html>
<html lang="en">
<head>
<meta charset="utf-8">
<title>The Meridale Bidding House</title>
<link href="https://fonts.googleapis.com/css2?family=Raleway:wght@500;600;700&family=Lato:wght@400;700&display=swap" rel="stylesheet">
<style>
:root{
  --red:#d21f3c;
  --navy:#35325e;
  --date:#0f2f7a;
  --ink:#222;
  --muted:#3c3a5e;
  --field:#e8e8e8;
  --field-line:#bfbfbf;
  --panel:#ebebeb;
  --footer:#262626;
  --base:#141414;
  --white:#fff;
}
*{box-sizing:border-box;margin:0;padding:0}
html,body{width:1200px;height:2830px;overflow:hidden}
body{position:relative;font-family:"Lato",Arial,sans-serif;color:var(--ink);background:var(--white)}
.abs{position:absolute}
h1,h2,h3{font-family:"Raleway",Arial,sans-serif}

/* header */
.site-header{top:0;left:0;width:1200px;height:136px;background:var(--white)}
.brand{left:52px;top:36px;display:flex;align-items:center;gap:12px}
.brand-dot{width:58px;height:58px;border-radius:50%;background:var(--red)}
.brand-name{font-family:"Raleway",sans-serif;font-weight:700;font-size:17px;color:var(--red);line-height:1.25;width:150px}
.address{right:430px;top:30px;text-align:right;font-size:13.5px;line-height:28px;color:var(--muted)}
.address-pin{left:786px;top:34px}
.contact{right:78px;top:26px;text-align:right;font-size:13.5px;line-height:27px;color:var(--muted)}
.contact-icons{left:1132px;top:30px;display:flex;flex-direction:column;gap:11px}

/* nav */
.main-nav{top:136px;left:0;width:1200px;height:64px;background:var(--red)}
.main-nav a{position:absolute;top:0;height:64px;line-height:64px;color:var(--white);font-size:13.5px;text-decoration:none}
.main-nav a.active{background:var(--navy);padding:0 20px}
.search{left:978px;top:16px;width:172px;height:28px;background:#f3f3f3;border:1px solid #ddd;font-size:11px;color:#aaa;padding:7px 8px}
.search svg{position:absolute;right:8px;top:6px}

/* hero */
.hero{top:200px;left:0;width:1200px;height:574px;background:linear-gradient(160deg,#5b5a4c 0%,#3f3f36 40%,#2b2f26 75%,#1f2a1c 100%)}
.hero-shade{inset:0;background:rgba(0,0,0,.35)}
.hero-title{top:150px;left:0;width:1200px;text-align:center;color:var(--white);font-weight:700;font-size:66px;line-height:82px}
.hero-title em{font-style:normal;color:var(--red)}
.hero-btn{left:495px;top:348px;width:210px;height:52px;background:var(--red);color:var(--white);font-size:19px;text-align:center;line-height:52px}

/* section titles */
.section-title{left:0;width:1200px;text-align:center;font-weight:600;font-size:32px;color:var(--ink)}
.section-title span{color:var(--red)}
.rule{height:1px;background:#cfcfcf}

/* featured */
.listing{width:200px;text-align:center}
.listing-img{width:160px;height:150px;margin:0 auto;border-radius:6px}
.listing p{margin-top:22px;font-size:15px;font-weight:700;color:#111}

/* newsletter */
.newsletter{top:1136px;left:0;width:1200px;height:274px;background:linear-gradient(180deg,#b63a4b,#c8324a 50%,#b42a40)}
.newsletter h2{top:58px;left:0;width:1200px;text-align:center;color:var(--white);font-size:34px;font-weight:700}
.nl-field{top:142px;height:48px;background:rgba(255,255,255,.55);font-size:11px;color:#555;padding:17px 14px}
.nl-btn{left:874px;top:142px;width:278px;height:48px;background:var(--navy);color:var(--white);font-size:17px;text-align:center;line-height:48px}

/* form */
.field{background:var(--field);border:1px solid var(--field-line);font-size:12px;color:#777;padding:12px 14px}
.captcha{left:315px;top:1640px;width:265px;height:60px;background:var(--red)}
.captcha-icons{left:0;top:0;width:30px;height:60px;background:#b81a34}
.captcha-code{left:60px;top:18px;font-size:20px;font-weight:700;color:#f6c5cd;text-decoration:line-through}
.captcha-refresh{right:0;top:0;width:78px;height:60px;background:#555}
.send{left:78px;top:1722px;width:1039px;height:52px;background:var(--red);color:var(--white);text-align:center;line-height:52px;font-size:19px;font-weight:700}

/* upcoming */
.upcoming{top:1811px;left:0;width:1200px;height:525px;background:var(--panel)}
.card{background:var(--white);box-shadow:0 6px 14px rgba(0,0,0,.18)}
.card-img{position:absolute;border-radius:4px}
.date{position:absolute;background:var(--date);color:var(--white);font-size:14px;text-align:center}
.arrow{width:38px;height:38px;border-radius:50%;background:#b3b3b3}
.arrow svg{position:absolute;left:12px;top:11px}

/* footer */
.site-footer{top:2336px;left:0;width:1200px;height:419px;background:var(--footer);color:var(--white)}
.foot-title{font-family:"Raleway",sans-serif;font-size:22px;font-weight:600;color:var(--red)}
.foot-text{font-size:14px;line-height:29px}
.foot-rule{height:1px;background:#666}
.vline{width:1px;background:#444}
.view-all{font-size:11px;color:var(--white)}
.badge{background:#d8d8d8}
.post{width:330px}
.post-thumb{position:absolute;left:0;top:0;width:52px;height:48px;background:linear-gradient(135deg,#8a8f95,#4c5560)}
.post-title{position:absolute;left:66px;top:0;font-size:14px;color:var(--red)}
.post-text{position:absolute;left:66px;top:19px;font-size:11px;line-height:16px;color:var(--white);width:262px}
.news-date{position:absolute;left:0;top:8px;font-size:14px;color:var(--red);line-height:19px;text-align:center}
.base{top:2755px;left:0;width:1200px;height:75px;background:var(--base);color:var(--white)}
.base p{position:absolute;left:0;width:1200px;top:28px;text-align:center;font-size:12px}
.social{top:22px;width:28px;height:28px;border:1px solid #bbb}
.social.hot{background:var(--red);border-color:var(--red)}
</style>
</head>
<body>

<header class="site-header abs">
  <div class="brand abs"><div class="brand-dot"></div><div class="brand-name">The Meridale Bidding House</div></div>
  <div class="address abs">THE MERIDALE BIDDING HOUSE<br>P.O. Box 582<br>Brinmoor, OK 35817</div>
  <svg class="address-pin abs" width="12" height="16" viewBox="0 0 12 16"><path d="M6 0a6 6 0 0 0-6 6c0 4.5 6 10 6 10s6-5.5 6-10a6 6 0 0 0-6-6zm0 8.5A2.5 2.5 0 1 1 6 3.5a2.5 2.5 0 0 1 0 5z" fill="#d21f3c"/></svg>
  <div class="contact abs">(800)615-3087 or (256)382-9061<br>(256)382-5148<br>info@meridale-bidding.example</div>
  <div class="contact-icons abs">
    <svg width="14" height="14" viewBox="0 0 14 14"><path d="M3 0l3 3-2 2c1 2 3 4 5 5l2-2 3 3-2 3C6 14 0 8 0 2z" fill="#d21f3c"/></svg>
    <svg width="14" height="14" viewBox="0 0 14 14"><rect x="3" y="0" width="8" height="4" fill="#d21f3c"/><rect x="0" y="5" width="14" height="9" rx="1" fill="#d21f3c"/><rect x="4" y="9" width="6" height="2" fill="#fff"/></svg>
    <svg width="14" height="12" viewBox="0 0 14 12"><rect width="14" height="12" rx="1" fill="#d21f3c"/><path d="M1 1l6 5 6-5" stroke="#fff" stroke-width="1.5" fill="none"/></svg>
  </div>
</header>

<nav class="main-nav abs">
  <a class="active" style="left:48px">Home</a>
  <a style="left:152px">Auction Calendar</a>
  <a style="left:315px">Auction Results</a>
  <a style="left:465px">For Sale</a>
  <a style="left:563px">Services</a>
  <a style="left:665px">About Us</a>
  <a style="left:775px">Contact Us</a>
  <div class="search abs">search<svg width="14" height="14" viewBox="0 0 14 14"><circle cx="6" cy="6" r="4.5" stroke="#999" stroke-width="1.6" fill="none"/><path d="M9.5 9.5L13 13" stroke="#999" stroke-width="1.6"/></svg></div>
</nav>

<section class="hero abs" role="img" aria-label="Photo of a two-storey suburban house with lawn at dusk">
  <div class="hero-shade abs"></div>
  <h1 class="hero-title abs">The Best Place<br>to <em>Buy and Sell!</em></h1>
  <div class="hero-btn abs">REGISTER NOW</div>
</section>

<section class="featured">
  <div class="rule abs" style="left:45px;top:825px;width:395px"></div>
  <div class="rule abs" style="left:770px;top:825px;width:385px"></div>
  <h2 class="section-title abs" style="top:802px"><span>Featured</span> Listings</h2>
  <div class="listing abs" style="left:90px;top:866px"><div class="listing-img" role="img" aria-label="Illustration of a white cottage" style="background:linear-gradient(180deg,#ddd,#f4f4f4 60%,#9fc48a)"></div><p>Lorem ipsum dolor</p></div>
  <div class="listing abs" style="left:380px;top:862px"><div class="listing-img" role="img" aria-label="Illustration of a red house" style="background:linear-gradient(180deg,#c9303a,#e04b4b 60%,#7cb061)"></div><p>Lorem ipsum dolor</p></div>
  <div class="listing abs" style="left:645px;top:858px"><div class="listing-img" role="img" aria-label="Illustration of a house with a red roof" style="background:linear-gradient(180deg,#d33a34,#f0f0f0 55%,#9aa3a8)"></div><p>Lorem ipsum dolor</p></div>
  <div class="listing abs" style="left:940px;top:858px"><div class="listing-img" role="img" aria-label="Small house model held in open hands" style="background:linear-gradient(180deg,#e07a3e,#f2d9c4 60%,#e8c4a8)"></div><p>Lorem ipsum dolor</p></div>
</section>

<section class="newsletter abs" role="img" aria-label="Red-toned photo of a house porch behind the newsletter form">
  <h2 class="abs">Join Our Newsletter!</h2>
  <div class="nl-field abs" style="left:48px;width:390px">Enter Your Name</div>
  <div class="nl-field abs" style="left:462px;width:390px">Enter Your Email id</div>
  <div class="nl-btn abs">SIGN UP</div>
</section>

<section class="register">
  <div class="rule abs" style="left:45px;top:1457px;width:440px"></div>
  <div class="rule abs" style="left:720px;top:1457px;width:435px"></div>
  <h2 class="section-title abs" style="top:1436px;font-size:27px"><span>Register</span> Form</h2>
  <div class="field abs" style="left:76px;top:1526px;width:507px;height:42px">Name</div>
  <div class="field abs" style="left:610px;top:1526px;width:507px;height:42px">Email id</div>
  <div class="field abs" style="left:76px;top:1582px;width:507px;height:42px">Phone</div>
  <div class="field abs" style="left:610px;top:1582px;width:507px;height:114px">Property Description</div>
  <div class="field abs" style="left:78px;top:1644px;width:206px;height:46px;padding-top:15px">Type the text</div>
  <div class="captcha abs">
    <div class="captcha-icons abs">
      <svg width="30" height="60" viewBox="0 0 30 60"><circle cx="15" cy="12" r="5" fill="none" stroke="#fff" stroke-width="1.5"/><path d="M10 28h4l4-3v10l-4-3h-4z" fill="#fff"/><circle cx="15" cy="48" r="5" fill="#fff"/></svg>
    </div>
    <div class="captcha-code abs">1234</div>
    <div class="captcha-refresh abs"><svg width="78" height="60" viewBox="0 0 78 60"><path d="M47 30a8 8 0 1 1-3-6.2" stroke="#fff" stroke-width="3" fill="none"/><path d="M41 19l6 4-6 4z" fill="#fff"/></svg></div>
  </div>
  <div class="send abs">SEND</div>
</section>

<section class="upcoming abs">
  <h2 class="section-title abs" style="top:32px;font-size:33px"><span>Upcoming</span> Auctions</h2>
  <div class="arrow abs" style="left:44px;top:224px"><svg width="14" height="16" viewBox="0 0 14 16"><path d="M10 2L4 8l6 6" stroke="#fff" stroke-width="2.4" fill="none"/></svg></div>
  <div class="arrow abs" style="left:1111px;top:218px"><svg width="14" height="16" viewBox="0 0 14 16"><path d="M4 2l6 6-6 6" stroke="#fff" stroke-width="2.4" fill="none"/></svg></div>

  <div class="card abs" style="left:104px;top:141px;width:272px;height:298px">
    <div class="card-img" role="img" aria-label="Small model house held in a hand" style="left:30px;top:30px;width:210px;height:160px;background:linear-gradient(180deg,#fff,#c9a87a 55%,#e7c9ad)"></div>
    <div class="date" style="left:19px;top:211px;width:231px;height:37px;line-height:37px">March - 23 - 2016</div>
  </div>
  <div class="card abs" style="left:414px;top:102px;width:352px;height:377px">
    <div class="card-img" role="img" aria-label="Model house resting on an open palm" style="left:30px;top:40px;width:292px;height:180px;background:linear-gradient(180deg,#fff,#d9c6a6 50%,#f0d8c6)"></div>
    <div class="date" style="left:37px;top:255px;width:286px;height:42px;line-height:42px">March - 28 - 2016</div>
  </div>
  <div class="card abs" style="left:821px;top:134px;width:270px;height:297px">
    <div class="card-img" role="img" aria-label="Model house with a red roof in cupped hands" style="left:30px;top:30px;width:210px;height:160px;background:linear-gradient(180deg,#fff,#d0523e 45%,#e8c4a8)"></div>
    <div class="date" style="left:23px;top:213px;width:231px;height:37px;line-height:37px">March - 13 - 2016</div>
  </div>
</section>

<footer class="site-footer abs">
  <h3 class="foot-title abs" style="left:48px;top:32px">Contact Us</h3>
  <div class="foot-rule abs" style="left:48px;top:74px;width:230px"></div>
  <div class="foot-text abs" style="left:48px;top:96px">123 Address line1, Address line 2<br>Country, 123456.<br>Freephone: +1 234 567 890<br>Telephone: +1 234 567 890<br>FAX: +1 555 206 4173</div>
  <div class="foot-text abs" style="left:48px;top:268px">E-mail: mail@samplelink.example</div>
  <div class="badge abs" style="left:48px;top:330px;width:46px;height:48px"></div>
  <div class="badge abs" style="left:136px;top:330px;width:50px;height:48px"></div>
  <div class="badge abs" style="left:218px;top:330px;width:50px;height:50px;border-radius:50%"></div>
  <div class="vline abs" style="left:330px;top:70px;height:320px"></div>

  <h3 class="foot-title abs" style="left:396px;top:32px">Events blog</h3>
  <div class="view-all abs" style="left:680px;top:62px">View All</div>
  <div class="foot-rule abs" style="left:396px;top:78px;width:330px"></div>
  <div class="post abs" style="left:406px;top:102px"><div class="post-thumb"></div><div class="post-title">Lorem ipsum dolor sit ame</div><div class="post-text">Give up alcohol if cancer runs in your family, do Halden study warns - The Westerly</div></div>
  <div class="foot-rule abs" style="left:396px;top:166px;width:330px"></div>
  <div class="post abs" style="left:406px;top:198px"><div class="post-thumb"></div><div class="post-title">Lorem ipsum dolor sit ame</div><div class="post-text">Give up alcohol if cancer runs in your family, do Halden study warns - The Westerly</div></div>
  <div class="foot-rule abs" style="left:396px;top:262px;width:330px"></div>
  <div class="post abs" style="left:406px;top:294px"><div class="post-thumb"></div><div class="post-title">Lorem ipsum dolor sit ame</div><div class="post-text">Give up alcohol if cancer runs in your family, do Halden study warns - The Westerly</div></div>
  <div class="foot-rule abs" style="left:396px;top:358px;width:330px"></div>
  <div class="vline abs" style="left:780px;top:70px;height:320px"></div>

  <h3 class="foot-title abs" style="left:812px;top:28px">Latest News</h3>
  <div class="view-all abs" style="left:1092px;top:60px">View All</div>
  <div class="foot-rule abs" style="left:812px;top:76px;width:326px"></div>
  <div class="post abs" style="left:812px;top:112px"><div class="news-date">17<br>Aug</div><div class="post-thumb" style="left:60px"></div><div class="post-text" style="left:122px;top:0;width:200px">Give up alcohol if cancer runs in your family, Halden study warns - The Westerly</div></div>
  <div class="foot-rule abs" style="left:812px;top:172px;width:326px"></div>
  <div class="post abs" style="left:812px;top:206px"><div class="news-date">17<br>Aug</div><div class="post-thumb" style="left:60px"></div><div class="post-text" style="left:122px;top:0;width:200px">Give up alcohol if cancer runs in your family, Halden study warns - The Westerly</div></div>
  <div class="foot-rule abs" style="left:812px;top:266px;width:326px"></div>
  <div class="post abs" style="left:812px;top:300px"><div class="news-date">17<br>Aug</div><div class="post-thumb" style="left:60px"></div><div class="post-text" style="left:122px;top:0;width:200px">Give up alcohol if cancer runs in your family, Halden study warns - The Westerly</div></div>
</footer>

<div class="base abs">
  <p>Copyright 2016 Company Name. All Rights Reserved.</p>
  <div class="social abs" style="left:1005px"></div>
  <div class="social abs" style="left:1040px"></div>
  <div class="social hot abs" style="left:1075px"></div>
  <div class="social abs" style="left:1110px"></div>
</div>

</body>
</html>
```